"Bright Hollow Craft Dwellings" need a busines Card Design got Builder

We need a business card design for a company based in Milford, Michigancalled Bright Hollow Craft Dwellings - has been recognized as a premier custom home builder. Distinguished by outstanding craftmanship and timeless beauty. Our custom home can be found in the most prestigious communities in Michigan. The homes are built with ICF (insulated concrete homes) which is green, allergy free, fire free, mold free and quitter. Our slogan "building one dream at a Time" and also we are ICF distributor for the state of Michigan

Target Market(s)

Anyone who is making over $100,000 a year and who wants to have totally custom built home. Ages from 29 up to 60 years old

Industry/Entity Type

Concrete

Contact Information for Business Card

we want to use - green, black, gray or blue colors - we want to look different with our business cards, because we built homes only with ICF, green, healthier and highly energy efficient homes.

Requirements
Must have
• I have logo that I attached and we have been using the logo (the only green home)
Nice to have
• should look quality business card,

```html
<!DOCTYPE html>
<html lang="en">
<head>
<meta charset="utf-8">
<title>Bright Hollow Craft Dwellings – Business Card</title>
<link href="https://fonts.googleapis.com/css2?family=Open+Sans:wght@400;600;700&display=swap" rel="stylesheet">
<style>
  :root {
    --backdrop: #e4e2de;
    --card-white: #ffffff;
    --card-shade: #e9e9ea;
    --ink: #2b2b2b;
    --ink-soft: #3a3a3a;
    --brand-gray: #8c8c8f;
    --brand-mark: #3d3a8a;
    --blue-deep: #2e4d9e;
    --blue-mid: #4d86cb;
    --blue-light: #6b9ad6;
  }
  * { box-sizing: border-box; margin: 0; padding: 0; }
  html, body {
    width: 1200px; height: 899px; overflow: hidden;
    background: var(--backdrop);
    font-family: "Open Sans", Arial, sans-serif;
  }
  .card {
    position: absolute; left: 100px; top: 164px;
    width: 1000px; height: 571px; overflow: hidden;
    background: radial-gradient(ellipse at 48% 55%, var(--card-white) 0%, #f6f6f6 45%, var(--card-shade) 100%);
    box-shadow: 0 10px 28px rgba(0,0,0,0.22);
  }
  .card__waves { position: absolute; inset: 0; width: 100%; height: 100%; }
  .brand {
    position: absolute; left: 64px; top: 58px;
    display: flex; align-items: center; gap: 14px;
  }
  .brand__dot {
    width: 46px; height: 46px; border-radius: 50%;
    background: var(--brand-mark); flex: none;
  }
  .brand__name {
    font-size: 19px; font-weight: 600; line-height: 1.15;
    color: var(--brand-gray); letter-spacing: 0.06em; text-transform: uppercase;
    width: 240px;
  }
  .contact {
    position: absolute; left: 64px; top: 196px;
    list-style: none; color: var(--ink-soft);
    font-size: 19px; line-height: 1.35;
  }
  .contact__item { display: flex; align-items: flex-start; gap: 10px; margin-bottom: 4px; }
  .contact__icon { width: 18px; height: 18px; flex: none; margin-top: 4px; }
  .person {
    position: absolute; right: 70px; bottom: 52px; text-align: right; color: var(--ink);
  }
  .person__name { font-size: 44px; font-weight: 700; line-height: 1.1; }
  .person__role { font-size: 38px; font-weight: 400; line-height: 1.2; }
</style>
</head>
<body>
<main class="card">
  <svg class="card__waves" viewBox="0 0 1000 571" preserveAspectRatio="none" aria-hidden="true">
    <path d="M440,0 C740,50 935,270 1000,480 L1000,0 Z" fill="var(--blue-mid)"/>
    <path d="M478,0 C760,46 945,260 1000,452 L1000,0 Z" fill="var(--card-white)" opacity="0.0"/>
    <path d="M520,0 C785,40 955,240 1000,405 L1000,0 Z" fill="var(--blue-deep)"/>
    <path d="M800,190 C900,280 960,360 1000,440" fill="none" stroke="var(--blue-light)" stroke-width="7"/>
  </svg>

  <div class="brand">
    <span class="brand__dot"></span>
    <span class="brand__name">Bright Hollow Craft Dwellings</span>
  </div>

  <ul class="contact">
    <li class="contact__item">
      <svg class="contact__icon" viewBox="0 0 18 18"><circle cx="9" cy="9" r="9" fill="var(--ink-soft)"/><path d="M4 9.5 9 5l5 4.5h-1.5V13h-2v-2.5h-3V13h-2V9.5z" fill="#fff"/></svg>
      <span>Suite # 118, Oak Bldg,<br>MI 48381</span>
    </li>
    <li class="contact__item">
      <svg class="contact__icon" viewBox="0 0 18 18"><circle cx="9" cy="9" r="9" fill="var(--ink-soft)"/><path d="M6 4.5c1 0 1.6 2 1.2 2.6l-.8.8c.6 1.3 1.5 2.2 2.8 2.8l.8-.8c.6-.4 2.6.2 2.6 1.2 0 1-1 2.1-2 2-3.6-.4-6.2-3-6.6-6.6 0-1 1-2 2-2z" fill="#fff"/></svg>
      <span>555-201-4410</span>
    </li>
    <li class="contact__item">
      <svg class="contact__icon" viewBox="0 0 18 18"><circle cx="9" cy="9" r="9" fill="var(--ink-soft)"/><rect x="6" y="3.5" width="6" height="11" rx="1" fill="#fff"/><rect x="7" y="5" width="4" height="6" fill="var(--ink-soft)"/></svg>
      <span>555-318-2206</span>
    </li>
    <li class="contact__item">
      <svg class="contact__icon" viewBox="0 0 18 18"><circle cx="9" cy="9" r="9" fill="var(--ink-soft)"/><rect x="4" y="7" width="10" height="6" rx="1" fill="#fff"/><rect x="6" y="4" width="6" height="3" fill="#fff"/></svg>
      <span>555-742-9031</span>
    </li>
    <li class="contact__item">
      <svg class="contact__icon" viewBox="0 0 18 18"><circle cx="9" cy="9" r="9" fill="var(--ink-soft)"/><rect x="4" y="5.5" width="10" height="7" fill="#fff"/><path d="M4 5.5 9 10l5-4.5" fill="none" stroke="var(--ink-soft)" stroke-width="1.2"/></svg>
      <span>hello@brighthollow.com</span>
    </li>
    <li class="contact__item">
      <svg class="contact__icon" viewBox="0 0 18 18"><circle cx="9" cy="9" r="9" fill="var(--ink-soft)"/><circle cx="9" cy="9" r="5" fill="none" stroke="#fff" stroke-width="1.2"/><path d="M4 9h10M9 4c-2.5 3-2.5 7 0 10M9 4c2.5 3 2.5 7 0 10" fill="none" stroke="#fff" stroke-width="1"/></svg>
      <span>www.brighthollowhomes.com</span>
    </li>
  </ul>

  <div class="person">
    <p class="person__name">Daniel Reyes</p>
    <p class="person__role">Owner / C.E.O</p>
  </div>
</main>
</body>
</html>
```